Verbena Home- Hang tags for Modern Handmade Home Decor products

We need to design some hang tags to use for our products, we want double tags, meaning two tags that go together on one string, two different and coordinating sizes and shapes. We have a logo, what we need is the artwork for these two tags to take to print. One tag will have the logo on one side and company information on the other, the second tag will be for product information. For example, we specialize in handmade pieces from Latin America, on the product tag I want space to write the product info but also a line for what country it's from and what community created it. I'm attaching an image of the shapes of tags that I like, along with a copy of our logo. On the larger company tag I'd like our logo in the center and a color block stripe of the yellow color of our logo at the bottom, on the flip side there will just be text, sort of our company motto. On the narrower longer product info tag I'd like a small logo at the bottom end and space for product information to be written in by hand and on the flip side of this one lines for what country it's from, what community created it and care instructions, again, all information that we will write in by hand. Please let me know if you have questions.

Target Market(s)

Design savvy, house proud, well educated people who travel and appreciate art.

Font styles to use
Sans Serif

Requirements
Must have
• I want it to look graphic, sophisticated and modern. I want to be very legible and clean.
Nice to have
• Clarity, easy to read, and maybe a bit of whimsy or lightheartedness.
Should not have
• Nothing that feels "ethnic" or "crafty:, even though our products are handmade in Latin America they are contemporary and sophisticated, not stereotypical.

```html
<!DOCTYPE html>
<html lang="en">
<head>
<meta charset="utf-8">
<title>Verbena Home — Hang Tags</title>
<link rel="stylesheet" href="https://fonts.googleapis.com/css2?family=Montserrat:wght@300;400&display=swap">
<style>
  :root {
    --paper: #ffffff;
    --tag-edge: #c4c7ca;
    --brand-yellow: #fccb0b;
    --brand-grey: #a9b6be;
    --write-line: #a7abaf;
  }
  html, body {
    margin: 0;
    padding: 0;
    width: 1200px;
    height: 665px;
    overflow: hidden;
    background: var(--paper);
  }
  .tag-sheet {
    display: block;
    width: 1200px;
    height: 665px;
  }
  .tag-outline {
    fill: var(--paper);
    stroke: var(--tag-edge);
    stroke-width: 1;
  }
  .string-hole {
    fill: var(--paper);
    stroke: #8d9195;
    stroke-width: 1;
  }
  .color-stripe { fill: var(--brand-yellow); }
  .brand-dot { fill: var(--brand-yellow); }
  .write-line {
    stroke: var(--write-line);
    stroke-width: 1;
    stroke-dasharray: 4 3;
  }
  .brand-name {
    font-family: "Montserrat", sans-serif;
    font-weight: 300;
    fill: var(--brand-grey);
    text-anchor: middle;
  }
  .brand-url {
    font-family: "Montserrat", sans-serif;
    font-weight: 400;
    fill: var(--brand-grey);
    text-anchor: middle;
  }
</style>
</head>
<body>
<svg class="tag-sheet" viewBox="0 0 1110 615" preserveAspectRatio="xMidYMid meet" aria-label="Verbena Home double hang tag set">
  <!-- Company tag, front -->
  <g class="company-tag-front">
    <path class="tag-outline" d="M15.5 52 L44 14.5 H259 L289.5 52 V454.5 H15.5 Z"/>
    <circle class="string-hole" cx="152" cy="39" r="7.5"/>
    <circle class="brand-dot" cx="152" cy="186" r="34"/>
    <text class="brand-name" x="152" y="272" font-size="30">Verbena Home</text>
    <text class="brand-url" x="152" y="294" font-size="9" letter-spacing="2.6">www.verbenahome.com</text>
    <rect class="color-stripe" x="15" y="435" width="275" height="20"/>
  </g>

  <!-- Company tag, back -->
  <g class="company-tag-back">
    <path class="tag-outline" d="M329.5 52 L359 14.5 H573 L603.5 52 V454.5 H329.5 Z"/>
    <circle class="string-hole" cx="466" cy="39" r="7.5"/>
    <line class="write-line" x1="375" y1="174.5" x2="558" y2="174.5"/>
    <line class="write-line" x1="375" y1="194.5" x2="558" y2="194.5"/>
    <line class="write-line" x1="375" y1="214.5" x2="558" y2="214.5"/>
    <line class="write-line" x1="375" y1="234.5" x2="558" y2="234.5"/>
    <line class="write-line" x1="375" y1="254.5" x2="558" y2="254.5"/>
    <line class="write-line" x1="375" y1="274.5" x2="558" y2="274.5"/>
  </g>

  <!-- Product tag, front -->
  <g class="product-tag-front">
    <path class="tag-outline" d="M642.5 72 L692 14.5 H798 L848.5 72 V601.5 H642.5 Z"/>
    <circle class="string-hole" cx="745" cy="39" r="7.5"/>
    <circle class="brand-dot" cx="745" cy="503" r="11"/>
    <text class="brand-name" x="745" y="533" font-size="10">Verbena Home</text>
    <text class="brand-url" x="745" y="541" font-size="3.5" letter-spacing="0.8">www.verbenahome.com</text>
    <line class="write-line" x1="674" y1="567.5" x2="816" y2="567.5"/>
  </g>

  <!-- Product tag, back -->
  <g class="product-tag-back">
    <path class="tag-outline" d="M889.5 72 L939 14.5 H1045 L1095.5 72 V601.5 H889.5 Z"/>
    <circle class="string-hole" cx="992" cy="39" r="7.5"/>
    <g class="origin-lines">
      <line class="write-line" x1="921" y1="164.5" x2="1063" y2="164.5"/>
      <line class="write-line" x1="921" y1="184.5" x2="1063" y2="184.5"/>
      <line class="write-line" x1="921" y1="204.5" x2="1063" y2="204.5"/>
      <line class="write-line" x1="921" y1="224.5" x2="1063" y2="224.5"/>
    </g>
    <g class="community-lines">
      <line class="write-line" x1="921" y1="264.5" x2="1063" y2="264.5"/>
      <line class="write-line" x1="921" y1="284.5" x2="1063" y2="284.5"/>
      <line class="write-line" x1="921" y1="304.5" x2="1063" y2="304.5"/>
      <line class="write-line" x1="921" y1="324.5" x2="1063" y2="324.5"/>
    </g>
    <g class="care-lines">
      <line class="write-line" x1="921" y1="364.5" x2="1063" y2="364.5"/>
      <line class="write-line" x1="921" y1="384.5" x2="1063" y2="384.5"/>
      <line class="write-line" x1="921" y1="404.5" x2="1063" y2="404.5"/>
      <line class="write-line" x1="919" y1="424.5" x2="1061" y2="424.5"/>
    </g>
  </g>
</svg>
</body>
</html>
```